Redesign existing website.

I need a holidayhouse webdisain. Please review existing website: www.sorvimaja.ee
I want to keep my logo.
Target Market(s)
Nature and sea enjoying holidaymakers, aged 30 to 70
Requirements
Must have
- 3 languages (English, Russian and Estonian)

```html
<!DOCTYPE html>
<html lang="et">
<head>
<meta charset="utf-8">
<title>Sorvimaja Puhkemaja – Hinnakiri</title>
<link href="https://fonts.googleapis.com/css2?family=Open+Sans:wght@400;600;700&family=Signika:wght@600&family=Figtree:wght@400;500&display=swap" rel="stylesheet">
<style>
:root{
  --sky-top:#0d63c9;
  --sky-mid:#3a8fe0;
  --nav-bg:#f2f2f2;
  --nav-text:#3a3a3a;
  --accent-yellow:#f9ee66;
  --button-border:#d8c92a;
  --button-text:#7a4a1a;
  --alert-red:#e3261b;
  --table-green:#00946f;
  --table-dark:#007c5c;
  --row-a:#e4e4e6;
  --row-b:#f0f0f2;
  --body-text:#222;
  --footer-bg:#353535;
  --white:#fff;
}
*{box-sizing:border-box;margin:0;padding:0}
html,body{width:1200px;height:1022px;overflow:hidden}
body{position:relative;font-family:"Figtree",Arial,sans-serif;color:var(--body-text);background:var(--white)}
.scenery{position:absolute;left:0;top:0;width:1200px;height:971px;
  background:
    linear-gradient(180deg,rgba(255,255,255,0) 55%,#fff 68%),
    linear-gradient(90deg,#3c6a2f 0%,#5b7e45 14%,rgba(90,150,220,0) 22%,rgba(90,150,220,0) 80%,#6e9ec9 82%,#9fc2de 100%),
    linear-gradient(180deg,var(--sky-top) 0%,var(--sky-mid) 35%,#8ab7e4 55%,#fff 70%);}
.scenery-sand{position:absolute;left:0;top:330px;width:228px;height:300px;
  background:linear-gradient(180deg,rgba(200,180,150,.8),rgba(255,255,255,1));}
.brand{position:absolute;left:232px;top:30px;display:flex;align-items:center;gap:18px;color:var(--white);font-family:"Open Sans",sans-serif;font-weight:600}
.brand-mark{width:70px;height:70px;border-radius:50%;background:var(--white);opacity:.9}
.brand-name{line-height:1.05}
.brand-name .main{display:block;font-size:26px;letter-spacing:.5px}
.brand-name .sub{display:block;font-size:18px;letter-spacing:1px;padding-left:18px}
.langs{position:absolute;top:25px;left:874px;display:flex;gap:7px}
.langs svg{display:block}
.contact{position:absolute;right:228px;top:78px;text-align:right;color:var(--white);font-family:"Open Sans",sans-serif;font-size:14px;line-height:21px}
.contact div{display:flex;align-items:center;justify-content:flex-end;gap:7px}
.nav{position:absolute;left:228px;top:133px;width:744px;height:38px;background:var(--nav-bg);display:flex;padding-left:50px;box-shadow:0 6px 6px -4px rgba(0,0,0,.35)}
.nav a{display:block;font-family:"Open Sans",sans-serif;font-weight:600;font-size:12.5px;color:var(--nav-text);text-decoration:none;line-height:38px;padding:0 23px}
.nav a.active{background:var(--accent-yellow);color:#222}
.panel{position:absolute;left:228px;top:186px;width:744px;height:785px;background:var(--white)}
.hero-frame{position:absolute;left:12px;top:12px;width:720px;height:296px;background:var(--white);box-shadow:0 2px 6px rgba(0,0,0,.35)}
.hero-photo{position:absolute;left:12px;top:12px;width:696px;height:272px;
  background:linear-gradient(90deg,#6a3a22 0%,#a9b6c4 18%,#d4dbe3 34%,#8e5a3a 52%,#c9b9a3 70%,#3a2a20 85%,#8a7260 100%)}
.title-button{position:absolute;left:244px;top:282px;width:256px;height:54px;background:var(--accent-yellow);border:2px solid var(--button-border);box-shadow:0 0 0 3px #f4eb7a inset,0 3px 5px rgba(0,0,0,.3);text-align:center;line-height:50px;font-family:"Signika",sans-serif;font-weight:600;font-size:17px;color:var(--button-text);letter-spacing:.5px}
.closed-note{position:absolute;left:0;top:360px;width:744px;text-align:center;font-family:"Signika",sans-serif;font-weight:600;font-size:21px;color:var(--alert-red);letter-spacing:.5px}
.prices{position:absolute;left:63px;top:401px;width:618px;border-collapse:collapse;font-size:13px}
.prices th{position:relative;height:60px;background:var(--table-green);color:var(--white);font-weight:500;line-height:17px;overflow:hidden}
.prices th.dark{background:var(--table-dark)}
.prices th + th,.prices td + td{border-left:1px solid var(--white)}
.prices th .flag{position:absolute;left:0;top:0;width:0;height:0;border-top:16px solid var(--alert-red);border-right:16px solid transparent}
.prices th .flag.y{border-top-color:var(--accent-yellow)}
.prices td{height:54px;text-align:center;border-top:1px solid var(--white)}
.prices td:first-child{text-align:left;padding-left:17px}
.prices tr:nth-child(odd) td{background:var(--row-a)}
.prices tr:nth-child(even) td{background:var(--row-b)}
.terms{position:absolute;left:63px;top:645px;width:620px;font-size:13px;line-height:18px}
.terms p{margin-bottom:17px}
.footer{position:absolute;left:0;top:971px;width:1200px;height:51px;background:var(--footer-bg);color:var(--white);text-align:center;font-family:Arial,sans-serif;font-size:11.5px;line-height:53px}
</style>
</head>
<body>
<div class="scenery" role="img" aria-label="Background photo of a sunny sandy beach with pine trees on the left and calm blue sea on the right"></div>
<div class="scenery-sand" aria-hidden="true"></div>

<header>
  <div class="brand">
    <span class="brand-mark"></span>
    <span class="brand-name"><span class="main">SORVIMAJA</span><span class="sub">PUHKEMAJA</span></span>
  </div>
  <div class="langs">
    <svg width="29" height="19" viewBox="0 0 29 19" aria-label="English"><rect width="29" height="19" fill="#fff"/><g fill="#c8102e"><rect y="0" width="29" height="1.5"/><rect y="3" width="29" height="1.5"/><rect y="6" width="29" height="1.5"/><rect y="9" width="29" height="1.5"/><rect y="12" width="29" height="1.5"/><rect y="15" width="29" height="1.5"/><rect y="17.5" width="29" height="1.5"/></g><rect width="12" height="10" fill="#1f3a8a"/></svg>
    <svg width="29" height="19" viewBox="0 0 29 19" aria-label="Русский"><rect width="29" height="6.3" fill="#fff"/><rect y="6.3" width="29" height="6.4" fill="#1c4fbf"/><rect y="12.7" width="29" height="6.3" fill="#d52b1e"/></svg>
    <svg width="29" height="19" viewBox="0 0 29 19" aria-label="Eesti"><rect width="29" height="6.3" fill="#1c72c9"/><rect y="6.3" width="29" height="6.4" fill="#000"/><rect y="12.7" width="29" height="6.3" fill="#fff"/></svg>
  </div>
  <div class="contact">
    <div>+372 55 12 345 <svg width="10" height="15" viewBox="0 0 10 15"><rect x="1" y="1" width="8" height="13" rx="1.5" fill="none" stroke="#f9ee66" stroke-width="1.6"/><circle cx="5" cy="11.5" r="0.9" fill="#f9ee66"/></svg></div>
    <div>info@sorvimaja.ee <svg width="14" height="10" viewBox="0 0 14 10"><rect x="0.5" y="0.5" width="13" height="9" fill="#f9ee66"/><path d="M0.5 0.5 L7 6 L13.5 0.5" fill="none" stroke="#0d63c9" stroke-width="1"/></svg></div>
  </div>
  <nav class="nav">
    <a href="#">TUTVUSTUS</a>
    <a href="#" class="active">HINNAKIRI</a>
    <a href="#">ASUKOHT</a>
    <a href="#">GALERII</a>
    <a href="#">HUVITAVAT</a>
    <a href="#">KONTAKT</a>
  </nav>
</header>

<main class="panel">
  <div class="hero-frame">
    <div class="hero-photo" role="img" aria-label="Interior photo of the holiday house with dining table, kitchenette and a lit fireplace"></div>
  </div>
  <div class="title-button">MEIE HINNAKIRI</div>
  <h1 class="closed-note">DETS, JAAN, VEEBR, MÄRTS - PUHKEMAJA SULETUD</h1>
  <table class="prices">
    <tr>
      <th style="width:203px"></th>
      <th class="dark" style="width:85px"><span class="flag"></span>Ööpäev<br>(1 night)</th>
      <th style="width:86px"><span class="flag y"></span>1 nädal<br>(1 week)</th>
      <th class="dark" style="width:140px"><span class="flag"></span>Nädalavahetus<br>Weekend Fr - Sun</th>
      <th><span class="flag y"></span>Ööbimine<br>paadis</th>
    </tr>
    <tr><td>mai, oktoober</td><td>75 EUR</td><td>405 EUR</td><td>200 EUR</td><td>-</td></tr>
    <tr><td>juuni, juuli, august, sept</td><td>95 EUR</td><td>450 EUR</td><td>215 EUR</td><td>20 EUR</td></tr>
    <tr><td>Rannamaja</td><td>90 EUR</td><td>450 EUR</td><td>200 EUR</td><td>-</td></tr>
  </table>
  <div class="terms">
    <p>Sisseregistreerimine, check in 15:00-18:00<br>Maja vabastatakse, check out 12:00</p>
    <p>Broneeringu annuleerimisel vähemalt nädal enne saabumispäeva tagastame ettemaksust 50%. Hilisema annuleerimise või külalise mitteilmumise korral ettemaksu ei tagastata.</p>
    <p>Sorvimaja Puhkemaja siseruumides ei suitsetata.</p>
  </div>
</main>

<footer class="footer">Copyright © 2014 www.sorvimaja.ee. All Rights Reserved.</footer>
</body>
</html>
```